Letterhead for Conveyancing Company

Use existing logo to create a letterhead for a conveyancing company. Must be able to be used in Microsoft Word. Easy to read and professional.
Contact information to be at the bottom.
Bright Wren Conveyancing Pty Ltd
ACN 621 984 736PO Box 535 Campbelltown SA 5074
Mobile - 0461273985
Web address - www.brightwrenconveyancing.com.au

Requirements
Must have
• Logo and contact details.
• Simple and professional.

```html
<!DOCTYPE html>
<html lang="en">
<head>
<meta charset="utf-8">
<title>Bright Wren Conveyancing Letterhead</title>
<link rel="stylesheet" href="https://fonts.googleapis.com/css2?family=Open+Sans:wght@400;600;700&family=Lato:wght@400&display=swap">
<style>
  :root {
    --pink: #e2409a;
    --ink: #444444;
    --ink-dark: #333333;
    --brand-grey: #7a7a7a;
    --rule: #9a9a9a;
    --paper: #ffffff;
    --backdrop: #e6e6e6;
  }
  * { margin: 0; padding: 0; box-sizing: border-box; }
  html, body { width: 1040px; height: 1200px; overflow: hidden; background: var(--backdrop); }
  .letterhead {
    position: absolute; left: 86px; top: 41px;
    width: 789px; height: 1016px;
    background: var(--paper);
    transform: scale(1.1); transform-origin: 0 0;
    font-family: "Open Sans", sans-serif; color: var(--ink);
  }
  .side-band {
    position: absolute; left: 0; top: 0; width: 23px; height: 967px;
    background: var(--pink);
    clip-path: polygon(0 0, 100% 26px, 100% 100%, 0 100%);
  }
  .side-block { position: absolute; left: 0; top: 977px; width: 23px; height: 19px; background: var(--pink); }
  .brand {
    position: absolute; left: 0; right: 0; top: 52px; text-align: center;
    font-family: "Open Sans", sans-serif; font-weight: 700; font-size: 30px;
    color: var(--brand-grey); letter-spacing: -0.5px;
  }
  .brand-mark { display: inline-block; width: 14px; height: 14px; background: var(--pink); margin-right: 10px; vertical-align: 3px; }
  .letter { position: absolute; left: 74px; width: 638px; font-size: 12.5px; line-height: 15px; }
  .issue-date { top: 183px; }
  .recipient { top: 214px; }
  .salutation { top: 302px; }
  .body-copy { top: 344px; line-height: 23px; text-align: justify; }
  .body-copy p + p { margin-top: 23px; }
  .closing { top: 690px; }
  .signatory { top: 755px; font-size: 16px; font-weight: 600; color: var(--ink-dark); }
  .signatory-role { top: 781px; }
  .footer { position: absolute; left: 0; right: 0; font-family: "Lato", sans-serif; color: #222; text-align: center; }
  .footer-contact { top: 949px; font-size: 14.5px; }
  .footer-rule { position: absolute; left: 101px; width: 586px; top: 972px; height: 1px; background: var(--rule); }
  .footer-company { top: 978px; font-size: 15px; }
  .accent { color: var(--pink); }
</style>
</head>
<body>
  <main class="letterhead">
    <div class="side-band"></div>
    <div class="side-block"></div>

    <div class="brand"><span class="brand-mark"></span>Bright Wren Conveyancing</div>

    <div class="letter issue-date">Issuing Date: May 5, 2018</div>
    <div class="letter recipient">Name Of Employee Mr. XYZABC<br>Address of Employee<br>Address Line 2 etc..</div>
    <div class="letter salutation">Dear Mr.XYZABC</div>

    <div class="letter body-copy">
      <p>Lorem Ipsum has been the industry's standard dummy text ever since the 1500s, when an unknown printer took a galley of type and scrambled it to make a type specimen book. It has survived not only five centuries, but also the leap into electronic typesetting, remaining essentially unchanged. It was popularised in the 1960s with the release of Letraset sheets containing Lorem Ipsum passages, and more recently with desktop publishing software like Aldus PageMaker including versions of Lorem Ipsum.</p>
      <p>Lorem Ipsum is simply dummy text of the printing and typesetting industry. Lorem Ipsum has been the industry's standard dummy text ever since the 1500s, when an unknown printer took a galley of type and scrambled it to make a type specimen book.</p>
      <p>It has survived not only five centuries, but also the leap into electronic typesetting, remaining essentially unchanged. It was popularised in the 1960s with the release of Letraset sheets containing Lorem IpsumIpsum passages.</p>
    </div>

    <div class="letter closing">Yours Sincerely</div>
    <div class="letter signatory">Daniel Hartley</div>
    <div class="letter signatory-role">Managing Director</div>

    <div class="footer footer-contact"><span class="accent">P:</span> 0461273985 &nbsp;|&nbsp; <span class="accent">www.brightwrenconveyancing.com.au</span></div>
    <div class="footer-rule"></div>
    <div class="footer footer-company"><span class="accent">Bright Wren Conveyancing Pty Ltd:</span>&nbsp; ACN 738 215 490 PO Box 862 Marlow Heights SA 5093</div>
  </main>
</body>
</html>
```